Blood Testing Health App

We are looking for a graphics designer to create a web app for us so that we may insert it into a health management website system.
For branding purposes we are at www.Veritamed.com and we are revamping our website... Example of new colors attached.
How we work...
We are a blood testing company based in the USA.
We offer a blood testing service nationwide in the USA.
We allow customers to order tests directly from us, visit a lab, have their blood drawn, or submit a urine sample, the lab tests it and they send the results back to our computer system and we share it with the customer.
The benefits of this are the customer does not need to go to the doctor and pay for the doctors visit to order these tests, which save them money. The tests are cheaper than going through the doctor. The customer simply uses us to get the test and the results and they can then take the results to their doctor... this process has saved them money. Others may be interested in regular check ups for blood work etc... and this allows them to do it with out needing a doctor, or if you have no insurance, this is a cheaper option too. We are quicker than a doctor, customers do not need appointments etc.
Hopefully you now have a better understanding as to what we do.
Here is the spec.
The app screen size is 750 px wide by 700 px high. ( A pdf is attached to show where the app is going to go, it is on page 3 of the pdf) The customer will have the ability to scroll… therefore the length of the page can be longer.
The app will consist of the following sections
Entry Page –
This will be the first page the user sees upon opening the app. This will be where they are directed from to the sections of the app discussed below. This needs to be branded for VeritaMed with a modern look.
1 – Order Test (Giving them the ability to purchase a blood test within the app)
2 – VeritaMed Dashboard (A dashboard that has everything they could need to use our service_
How it works Section on entry page – this will be a simple set of graphics showing how the service works. We already have the graphics for this, they do not need to be built again. They are attached to this brief
Basic structure of sections –
Order Test –
This page contains all tests, filed in categories – and Sub categories – Each test needs a link to an Information section – Price – Buy Now – Cart Process
VeritaMed Dashboard –
A page of icons along the top of the app
- My Confirmation
- My Nearest Lab
- My Receipt
- My Orders
- My Account
- My Results
- My Inbox
- Contact Us
Sections in more detail -
Order A Test –
Show all categories/ sub categories – There are 23 categories, 14 sub categories, and within these categories are 300 tests - Here is the information for the categories etc - http://www.veritamed.com/panels.aspx?PanelGroupID=4 Just in case it helps :)
We need to present this in a graphic format that is spacious, modern (quillbox, taskhub web appearance is the direction we are going for) We need it to be clear and not overwhelming to the customer.
Functionality idea…
Customer clicks category/ subcategory and tests appear.
Customer sees small 35 word description. For more information the test opens into a lightbox or expand the container which ever graphic designer believes to be most visually appealing
Buy Now must always be visible, along with price of the test
Buying process explained – Customer clicks buy now –
They are then taken to a Review Order screen ( This contains Order summary and choose payment method – insert payment details )
– Confirm payment –
Confirmation screen appears, thanking them.
They are then taken to the VeritaMed Dashboard...
VeritaMed Dashboard –
"My Confirmation" - Print Confirmation Order (PDF is in brief, we want this web based not a pdf download)
"My Nearest Lab Location" - This does not need to be designed because the web developer has this part under control, but we do need the icon in the dashboard
"My Receipt" - Print receipt - This does not exist in our system yet. So we need to create this from scratch - It will need to have - The test they are purchasing and the amount of the test - The customers name - The order ID - Must provide printer friendly option too
"My Orders" - This will have a list of orders - At the end of each order will be a status update of either "Test results" "Open order"
A graphic table format would be perfect. This will be linked to relevant results if they have been received. I have also attached a version of what the customer currently sees on our website. We know it is nasty ;) We are redesigning... but the information is there for this section to help design it with the right info. If the results are ready it will say in this list.
"Results Ready" will be a link to show those results once the customer has clicked the link, and the results will appear in the app, under the icons. There must be a printer friendly version too.
"My Results" Developer will sort this page out but we need the icon... It will be exactly like my orders but only show test results
"My Account" - This will be a place for them to update their personal information - Name, DOB, Address, Email Address
"My Inbox" - An inbox interface - Our way of contacting the customer for promotions we are running etc – We need a design of how this screen will appear. We also need the icon in the dashboard to have a notification on it if there are messages in the customers inbox. A little red 1, or circle with number of messages in the inbox.
"Customer Service" - This does not need to be designed because the web developer has this part under control, but we do need the icon in the dashboard
Icons appear along the top of app ( example - Mac icons/ iphone app icons) When the customer clicks an icon the content always appears below the icons
Here is more information for the icons and what should appear when each icon is clicked.
Screens to be designed –
Entry Page
Order A Test Page
Review Order Screen/Payment Screen - Show a lightbox that shows payment has been confirmed. Customer clicks close and are on the Confirmation Screen
VeritaMed Dashboard - Screens mentioned in detail above
We can't wait to see your designs!
Please email any questions.
Hi all this is the first time we have used pixel forum and understand the budget was too low for this project. We have now increased the budget to $2,000 and extended the deadline by another week
Hi all we are receiving some really great designs. I just added an example of the space that the web app will be going into... It is called "kelvraapp.pdf"
Hi guys updated the brief. Hopefully this will help with the dashboard part of the design

```html
<!DOCTYPE html>
<html lang="en">
<head>
<meta charset="utf-8">
<title>VeritaMed – Order a Test</title>
<link rel="stylesheet" href="https://fonts.googleapis.com/css2?family=Ubuntu:wght@400;500;700&display=swap">
<style>
:root{
  --ink:#333533;
  --ink-soft:#3f413f;
  --muted:#9a9c9b;
  --brand:#7dc242;
  --tab-bg:#ececec;
  --bar-top:#f1f1f1;
  --bar-bottom:#dcdcdc;
  --field:#ffffff;
  --button-dark:#3d3f3e;
  --icon-dark:#5a5d5b;
  --page:#ffffff;
}
*{box-sizing:border-box;margin:0;padding:0}
html,body{width:667px;height:1200px;overflow:hidden;background:var(--page)}
body{font-family:"Ubuntu",sans-serif;color:var(--ink);position:relative}

.app-header{position:absolute;left:0;top:0;width:667px;height:89px}
.brand{position:absolute;left:15px;top:40px;display:flex;align-items:center;gap:9px}
.brand-name{font-size:37px;font-weight:400;color:var(--ink);letter-spacing:-0.5px;line-height:1}
.brand-mark{width:24px;height:24px;background:var(--brand)}

.nav-tab{position:absolute;top:26px;height:63px;text-align:center;font-size:9.5px;text-transform:uppercase;letter-spacing:.2px}
.nav-tab svg{display:block;margin:12px auto 7px}
.nav-tab--active{left:302px;width:110px;background:var(--tab-bg);border-radius:8px 8px 0 0;color:var(--brand)}
.nav-tab--idle{left:414px;width:93px;color:var(--muted)}

.social{position:absolute;top:56px;left:557px;display:flex;gap:8px}
.social-dot{width:26px;height:26px;border-radius:50%;background:var(--brand)}

.category-bar{position:absolute;left:0;top:89px;width:667px;height:60px;
  background:linear-gradient(var(--bar-top),var(--bar-bottom));border-bottom:1px solid #d2d2d2}
.category-label{position:absolute;left:23px;top:21px;font-size:15px;font-weight:700;color:var(--ink-soft)}
.select{position:absolute;left:153px;top:18px;width:178px;height:27px;background:var(--field);
  border-radius:4px;font-size:12px;padding:6px 12px;color:var(--ink)}
.select-arrow{position:absolute;right:10px;top:9px}
.search{position:absolute;left:428px;top:18px;width:213px;height:27px;background:var(--field);
  border-radius:4px;font-size:12px;padding:6px 14px;color:var(--ink)}
.search-button{position:absolute;right:4px;top:4px;width:28px;height:19px;background:var(--button-dark);border-radius:4px}
.search-button svg{display:block;margin:3px auto}

.category-grid{position:absolute;left:0;top:205px;width:667px;display:grid;
  grid-template-columns:repeat(4,166.75px);grid-auto-rows:160px}
.category{display:flex;flex-direction:column;align-items:center;text-align:center}
.category-badge{width:98px;height:98px;border-radius:50%;
  background:radial-gradient(circle at 50% 30%,#ffffff 0%,#f1f1f1 45%,#cfd0cf 100%);
  box-shadow:inset 0 0 0 1px #c9cac9,0 3px 0 #8f918f,0 4px 4px rgba(0,0,0,.18);
  display:flex;align-items:center;justify-content:center}
.category-icon{width:62px;height:62px;fill:var(--icon-dark)}
.category-art{width:58px;height:62px;border-radius:40% 40% 14px 14px;
  background:linear-gradient(#7a7d7b,var(--icon-dark))}
.category-name{margin-top:9px;font-size:13.5px;line-height:17px;color:var(--ink)}
</style>
</head>
<body>

<header class="app-header">
  <div class="brand">
    <span class="brand-name">VeritaMed</span>
    <span class="brand-mark"></span>
  </div>

  <div class="nav-tab nav-tab--active">
    <svg width="28" height="20" viewBox="0 0 28 20"><rect x="4" y="1" width="20" height="13" rx="1.5" fill="none" stroke="#7dc242" stroke-width="2.2"/><rect x="1" y="15" width="26" height="3" rx="1" fill="#7dc242"/></svg>
    Order a test
  </div>
  <div class="nav-tab nav-tab--idle">
    <svg width="24" height="22" viewBox="0 0 24 22"><rect x="7" y="1" width="15" height="13" fill="none" stroke="#a3a5a4" stroke-width="2"/><rect x="2" y="7" width="15" height="13" fill="#fff" stroke="#a3a5a4" stroke-width="2"/></svg>
    Dashboard
  </div>

  <div class="social" aria-label="Social links">
    <span class="social-dot"></span><span class="social-dot"></span><span class="social-dot"></span>
  </div>
</header>

<section class="category-bar">
  <span class="category-label">Select Category</span>
  <div class="select">Allergies
    <svg class="select-arrow" width="13" height="11" viewBox="0 0 13 11"><path d="M0 0H13L6.5 11Z" fill="#333"/></svg>
  </div>
  <div class="search">Search for a test
    <span class="search-button"><svg width="16" height="13" viewBox="0 0 16 13"><circle cx="6" cy="5.5" r="4" fill="none" stroke="#fff" stroke-width="1.8"/><path d="M9 8l5 4" stroke="#fff" stroke-width="2.2" stroke-linecap="round"/></svg></span>
  </div>
</section>

<main class="category-grid">
  <div class="category"><div class="category-badge"><span class="category-art" role="img" aria-label="Male torso silhouette with heartbeat"></span></div><p class="category-name">Men's Health</p></div>
  <div class="category"><div class="category-badge"><span class="category-art" role="img" aria-label="Female torso silhouette with heartbeat"></span></div><p class="category-name">Women's Health</p></div>
  <div class="category"><div class="category-badge">
    <svg class="category-icon" viewBox="0 0 62 62" aria-label="First aid kit"><path d="M23 14h16v6h-4v-3h-8v3h-4z"/><rect x="10" y="20" width="42" height="30" rx="3"/><path d="M28 25h6v7h7v6h-7v7h-6v-7h-7v-6h7z" fill="#fff"/></svg>
  </div><p class="category-name">Most Common</p></div>
  <div class="category"><div class="category-badge">
    <svg class="category-icon" viewBox="0 0 62 62" aria-label="Virus"><circle cx="31" cy="31" r="16"/><g stroke="#5a5d5b" stroke-width="1.6"><path d="M31 8v6M31 48v6M8 31h6M48 31h6M15 15l4 4M43 43l4 4M47 15l-4 4M15 47l4-4M20 10l2 5M40 52l2-5M10 21l5 2M52 41l-5-2M42 10l-2 5M22 52l-2-5M52 21l-5 2M10 41l5-2"/></g></svg>
  </div><p class="category-name">Sexually Transmitted<br>Diseases</p></div>

  <div class="category"><div class="category-badge">
    <svg class="category-icon" viewBox="0 0 62 62" aria-label="Test lancet and blood drop"><rect x="12" y="10" width="8" height="26" rx="2" transform="rotate(-35 16 23)"/><path d="M38 22c0 0 9 12 9 19a9 9 0 0 1-18 0c0-7 9-19 9-19z"/></svg>
  </div><p class="category-name">Diabetes Detection &amp;<br>Management</p></div>
  <div class="category"><div class="category-badge"><span class="category-art" role="img" aria-label="Head in profile sneezing"></span></div><p class="category-name">Allergies</p></div>
  <div class="category"><div class="category-badge">
    <svg class="category-icon" viewBox="0 0 62 62" aria-label="Stethoscope"><path d="M14 10v14a10 10 0 0 0 20 0V10" fill="none" stroke="#5a5d5b" stroke-width="4"/><path d="M24 34v8a8 8 0 0 0 16 0v-4" fill="none" stroke="#5a5d5b" stroke-width="4"/><circle cx="42" cy="32" r="8"/><circle cx="42" cy="32" r="3.5" fill="#eee"/></svg>
  </div><p class="category-name">Specialized</p></div>
  <div class="category"><div class="category-badge"><span class="category-art" role="img" aria-label="Liver organ shape" style="border-radius:50% 20% 50% 40%"></span></div><p class="category-name">Hepatitis &amp;<br>Liver Function</p></div>

  <div class="category"><div class="category-badge">
    <svg class="category-icon" viewBox="0 0 62 62" aria-label="Heart with pulse line"><path d="M31 52C14 40 8 32 8 22a11 11 0 0 1 23-4 11 11 0 0 1 23 4c0 10-6 18-23 30z"/><path d="M4 31h14l4-8 5 16 5-20 5 16 4-4h17" fill="none" stroke="#fff" stroke-width="2.4"/></svg>
  </div><p class="category-name">Heart &amp; Stroke</p></div>
  <div class="category"><div class="category-badge">
    <svg class="category-icon" viewBox="0 0 62 62" aria-label="Syringe and pill"><g transform="rotate(45 31 31)"><rect x="25" y="8" width="12" height="30" rx="1"/><rect x="20" y="6" width="22" height="4"/><rect x="29.5" y="38" width="3" height="14"/></g><circle cx="19" cy="45" r="8"/><path d="M13 50l12-10" stroke="#eee" stroke-width="2"/></svg>
  </div><p class="category-name">Drugs &amp; Alcohol</p></div>
  <div class="category"><div class="category-badge">
    <svg class="category-icon" viewBox="0 0 62 62" aria-label="Capsules"><rect x="8" y="18" width="16" height="34" rx="8"/><rect x="28" y="8" width="16" height="40" rx="8" transform="rotate(45 36 28)" fill="none" stroke="#5a5d5b" stroke-width="3"/><path d="M31 32l12-12 3 3c4 4 4 9 0 12l-3 3z"/></svg>
  </div><p class="category-name">Nutrition &amp; Vitamins</p></div>
  <div class="category"><div class="category-badge">
    <svg class="category-icon" viewBox="0 0 62 62" aria-label="Awareness ribbon"><path d="M24 8h14l4 8-20 38-7-5 12-20-7-13z"/><path d="M34 30l13 19-7 5-10-17z"/></svg>
  </div><p class="category-name">Cancer Screening</p></div>

  <div class="category"><div class="category-badge">
    <svg class="category-icon" viewBox="0 0 62 62" aria-label="Poison bottle with warning cross"><rect x="24" y="6" width="14" height="8"/><path d="M20 14h22v6l6 6v28H14V26l6-6z"/><path d="M22 30l18 16M40 30L22 46" stroke="#fff" stroke-width="3"/></svg>
  </div><p class="category-name">Metals &amp; Poisoning</p></div>
  <div class="category"><div class="category-badge">
    <svg class="category-icon" viewBox="0 0 62 62" aria-label="Bathroom scale"><rect x="9" y="9" width="44" height="44" rx="6" fill="none" stroke="#5a5d5b" stroke-width="4"/><rect x="23" y="13" width="16" height="7" rx="2"/><ellipse cx="23" cy="37" rx="5" ry="9"/><ellipse cx="39" cy="37" rx="5" ry="9"/></svg>
  </div><p class="category-name">Weight Loss &amp; Fitness</p></div>
  <div class="category"><div class="category-badge">
    <svg class="category-icon" viewBox="0 0 62 62" aria-label="Molecule rings"><path d="M8 30l8-14h14l7 14-7 13H16z"/><path d="M30 16l8-8h12l6 12-6 12H38l-8-16z" fill="none" stroke="#5a5d5b" stroke-width="3"/></svg>
  </div><p class="category-name">Hormone</p></div>
  <div class="category"><div class="category-badge">
    <svg class="category-icon" viewBox="0 0 62 62" aria-label="Medical cross"><path d="M24 10h14v14h14v14H38v14H24V38H10V24h14z"/></svg>
  </div><p class="category-name">Autoimmune Disorders<br>/ Arthritis</p></div>

  <div class="category"><div class="category-badge"><span class="category-art" role="img" aria-label="Neck and shoulders silhouette showing thyroid"></span></div><p class="category-name">Thyroid / Parathyroid</p></div>
  <div class="category"><div class="category-badge">
    <svg class="category-icon" viewBox="0 0 62 62" aria-label="IV drip bag"><path d="M18 6h26v28c0 6-5 10-13 10s-13-4-13-10z" fill="none" stroke="#5a5d5b" stroke-width="3"/><path d="M20 18h22v16c0 5-4 8-11 8s-11-3-11-8z"/><rect x="29.5" y="44" width="3" height="14"/></svg>
  </div><p class="category-name">Infectious Disease</p></div>
  <div class="category"><div class="category-badge">
    <svg class="category-icon" viewBox="0 0 62 62" aria-label="Blood drop on test slide"><path d="M6 44l40-22 10 6-40 22z"/><path d="M20 8s10 14 10 21a10 10 0 0 1-20 0c0-7 10-21 10-21z"/></svg>
  </div><p class="category-name">Blood disease</p></div>
  <div class="category"><div class="category-badge"><span class="category-art" role="img" aria-label="Stomach organ shape" style="border-radius:20% 50% 50% 50%"></span></div><p class="category-name">Digestive disorders</p></div>

  <div class="category"><div class="category-badge">
    <svg class="category-icon" viewBox="0 0 62 62" aria-label="Kidneys"><ellipse cx="18" cy="30" rx="11" ry="17"/><ellipse cx="44" cy="30" rx="11" ry="17"/></svg>
  </div><p class="category-name">Kidney<br>/ Adrenal Gland</p></div>
  <div class="category"><div class="category-badge"><span class="category-art" role="img" aria-label="Pregnant figure silhouette"></span></div><p class="category-name">Pregnancy &amp; Fertility</p></div>
</main>

</body>
</html>
```